New Alcoholic Spiked Seltzer Line

We need a can design for a line of low calorie alcoholic seltzer. This product is a sparkling water and vodka drink with no sugar added in a slim 12 oz can.

This is a lighter, healthier, alternative to the sugary ready-to-drinks on the market. The product contains only 3 ingredients: Vodka, Water and Natural Flavors. It has only 100 calories but still has 5% alcohol, so you don't need to sacrifice alcohol to cut calories.

This product also does not contain any preservatives.

We want this design to communicate the following objectives to the consumer and in this order:

1. Appetizing product
2.Low calorie
3.Communicate the type of beverage (Spiked Seltzer)

The brand name of the product is VELKA.

The flavor of the product needed to be used for the design is Mango-Orange.

Comparable products are:

www.brisavelfizz.example/
https://www.tarnowbubble.example
https://quellrind.example/

The designs should not infringe or copy the creative directions of the products mentionned above. They are only given so that you can better understand the type of product we are developing.

Target Market(s)

Young Professional women between the ages of 25 and 44

Industry/Entity Type

Product

Colors

Designer to choose colors to be used in the design.

Requirements
Must have
• Design extendibility, meaning it can be adapted for other flavors.
• This is a new category in the market we are targeting, so consumers must easily be able to identify what type of product this is.

```html
<!DOCTYPE html>
<html lang="en">
<head>
<meta charset="UTF-8">
<title>VELKA Seltzer – Can Label Range</title>
<link rel="stylesheet" href="https://fonts.googleapis.com/css2?family=Playfair+Display:ital,wght@0,900;1,800&family=Josefin+Sans:wght@600;700&family=Oswald:wght@300&display=swap">
<style>
  :root {
    --canvas-bg: #ffffff;
    --label-bg: #ffffff;
    --label-edge: #e3e3e6;

    --mango: #ec7a1c;
    --mango-deep: #e2602a;
    --orange-yellow: #f2c21a;

    --raspberry: #d8264f;
    --raspberry-deep: #b0204f;
    --lime: #7cae2c;
    --lime-light: #c3d84a;

    --blackberry: #553063;
    --blackberry-light: #8a6a99;
    --apple: #7fb58f;
    --apple-light: #b9dcc2;
  }

  * { box-sizing: border-box; margin: 0; padding: 0; }

  html, body {
    width: 1200px;
    height: 1000px;
    overflow: hidden;
    background: var(--canvas-bg);
  }

  .range {
    position: relative;
    width: 1200px;
    height: 1000px;
  }

  .label {
    position: absolute;
    top: 200px;
    width: 262px;
    height: 670px;
    background: var(--label-bg);
    border: 1px solid var(--label-edge);
    border-radius: 14px;
    text-align: center;
  }
  .label--mango     { left: 155px; --primary: var(--mango);      --secondary: var(--mango-deep);      --tertiary: var(--orange-yellow); }
  .label--raspberry { left: 467px; --primary: var(--raspberry);  --secondary: var(--lime);            --tertiary: var(--lime-light); }
  .label--blackberry{ left: 779px; --primary: var(--blackberry); --secondary: var(--apple);           --tertiary: var(--apple-light); }

  .claims {
    position: absolute;
    top: 56px;
    left: 42px;
    text-align: left;
    color: var(--primary);
  }
  .claims__calories {
    display: block;
    font-family: "Playfair Display", serif;
    font-style: italic;
    font-weight: 800;
    font-size: 15px;
    line-height: 1;
    border-bottom: 1.5px solid var(--secondary);
    padding-bottom: 1px;
  }
  .claims__natural {
    display: block;
    font-family: "Josefin Sans", sans-serif;
    font-weight: 600;
    font-size: 11px;
    margin-top: 3px;
  }

  .brand {
    position: absolute;
    top: 168px;
    left: 0;
    right: 0;
    font-family: "Playfair Display", serif;
    font-weight: 900;
    font-size: 56px;
    line-height: 1;
    letter-spacing: 1px;
    color: var(--primary);
  }

  .category {
    position: absolute;
    top: 236px;
    left: 0;
    right: 0;
    font-family: "Josefin Sans", sans-serif;
    font-weight: 700;
    font-size: 17px;
    letter-spacing: 1.5px;
    color: var(--primary);
  }

  .flavour {
    position: absolute;
    top: 284px;
    left: 0;
    right: 0;
    font-family: "Josefin Sans", sans-serif;
    font-weight: 700;
    font-size: 14px;
    letter-spacing: 3px;
  }
  .flavour__main { color: var(--primary); }
  .flavour__plus,
  .flavour__second { color: var(--secondary); }

  .fruit-art {
    position: absolute;
    top: 338px;
    left: 16px;
    width: 230px;
    height: 230px;
    border-radius: 50%;
    background: radial-gradient(circle at 50% 50%, var(--tertiary) 0%, var(--primary) 55%, var(--secondary) 100%);
    opacity: 0.9;
  }

  .volume {
    position: absolute;
    top: 608px;
    left: 0;
    right: 0;
    font-family: "Oswald", sans-serif;
    font-weight: 300;
    font-size: 15px;
    letter-spacing: 0.5px;
    color: var(--primary);
  }
</style>
</head>
<body>
  <main class="range">

    <section class="label label--mango">
      <p class="claims">
        <span class="claims__calories">100 calories</span>
        <span class="claims__natural">Natural Flavours</span>
      </p>
      <h1 class="brand">VELKA</h1>
      <p class="category">SELTZER</p>
      <p class="flavour"><span class="flavour__main">MANGO</span><span class="flavour__plus">+</span><span class="flavour__second">ORANGE</span></p>
      <div class="fruit-art" role="img" aria-label="Four mango and orange slices arranged in a cross with small droplet shapes"></div>
      <p class="volume">12 FL OZ (355ML)</p>
    </section>

    <section class="label label--raspberry">
      <p class="claims">
        <span class="claims__calories">100 calories</span>
        <span class="claims__natural">Natural Flavours</span>
      </p>
      <h2 class="brand">VELKA</h2>
      <p class="category">SELTZER</p>
      <p class="flavour"><span class="flavour__main">RASPBERRY</span><span class="flavour__plus">+</span><span class="flavour__second">LIME</span></p>
      <div class="fruit-art" role="img" aria-label="Four raspberry and lime slices arranged in a cross with small droplet shapes"></div>
      <p class="volume">12 FL OZ (355ML)</p>
    </section>

    <section class="label label--blackberry">
      <p class="claims">
        <span class="claims__calories">100 calories</span>
        <span class="claims__natural">Natural Flavours</span>
      </p>
      <h2 class="brand">VELKA</h2>
      <p class="category">SELTZER</p>
      <p class="flavour"><span class="flavour__main">BLACKBERRY</span><span class="flavour__plus">+</span><span class="flavour__second">APPLE</span></p>
      <div class="fruit-art" role="img" aria-label="Four blackberry and apple slices arranged in a cross with small droplet shapes"></div>
      <p class="volume">12 FL OZ (355ML)</p>
    </section>

  </main>
</body>
</html>
```